Professional Law Firm Rebranding Brochure Layout Design

Our law firm is changing its name from The Law Office of Dana Moreno, PLLC to MORENO.LAW. I would like a 4-page color brochure (cover, page 2, page 3, back) that announces and explains our rebranding. I have attached lots of files that should be helpful. I envision the words "The Law Office of Dana Moreno, PLLC is now known as MORENO.LAW" at the top of the front cover. Feel free to review our website at https://moreno-legal.example to get an idea of the look and feel we like. Tall buildings and other professional images work well.

Target Market(s)

Businesses, law firm clients, entrepreneurs, startups, corporations

Industry/Entity Type

Legal

Font styles to use
Sans Serif

Colors
cfdeed
85abd2
3276b5
0555a3
cee9f5
85cae6
33a6d7
0492cd

Requirements
Must have
• Professional appearance, photos & bios of team members, explanation of rebranding - finished product is US letter size

```html
<!DOCTYPE html>
<html lang="en">
<head>
<meta charset="utf-8">
<title>MORENO.LAW Rebranding Brochure – Back and Front Cover</title>
<link rel="stylesheet" href="https://fonts.googleapis.com/css2?family=Lato:wght@400;700;900&family=Roboto+Condensed:wght@400;700&display=swap">
<style>
  :root {
    --stage: #4c4946;
    --paper: #ffffff;
    --navy: #173f88;
    --brand-blue: #0555a3;
    --sky: #6cb6dd;
    --mist: #c5d2ea;
    --ice: #cee9f5;
    --ink: #222222;
    --muted: #4a4a4a;
  }
  html, body {
    margin: 0;
    width: 1200px;
    height: 1010px;
    overflow: hidden;
    background: var(--stage);
  }
  .spread {
    position: absolute;
    left: 64px;
    top: 158px;
    width: 1072px;
    height: 693px;
    display: block;
  }
  .heading-bold { font: 900 28px "Lato", sans-serif; fill: #fff; }
  .heading-light { font: 400 28px "Lato", sans-serif; fill: #fff; }
  .office-name { font: 700 15px "Roboto Condensed", sans-serif; fill: var(--navy); }
  .office-line { font: 400 14.5px "Roboto Condensed", sans-serif; fill: var(--ink); }
  .contact-item { font: 400 14.5px "Roboto Condensed", sans-serif; fill: var(--ink); text-anchor: middle; }
  .tagline-bold { font: 900 27px "Lato", sans-serif; fill: var(--navy); }
  .tagline-light { font: 400 27px "Lato", sans-serif; fill: var(--navy); }
  .tagline-large { font: 400 33px "Lato", sans-serif; fill: var(--navy); text-anchor: middle; }
  .web-link { font: 400 17px "Lato", sans-serif; fill: #dbe6f6; }
  .announce { font: 400 13.5px "Lato", sans-serif; fill: var(--muted); text-anchor: middle; }
  .brand-name { font: 700 42px "Lato", sans-serif; fill: var(--brand-blue); }
  .icon { fill: none; stroke: var(--sky); stroke-width: 1.4; }
</style>
</head>
<body>
<svg class="spread" viewBox="0 0 1322 855" xmlns="http://www.w3.org/2000/svg">
  <defs>
    <linearGradient id="tower-tones" x1="0" y1="0" x2="1" y2="1">
      <stop offset="0" stop-color="#6fa3b4"/>
      <stop offset="0.35" stop-color="#2d6a93"/>
      <stop offset="0.7" stop-color="#1c4a73"/>
      <stop offset="1" stop-color="#3f5f86"/>
    </linearGradient>
    <linearGradient id="desk-tones" x1="0" y1="0" x2="1" y2="1">
      <stop offset="0" stop-color="#dfe8ef"/>
      <stop offset="0.45" stop-color="#c4d1dc"/>
      <stop offset="0.8" stop-color="#eef2f6"/>
      <stop offset="1" stop-color="#f4e7d6"/>
    </linearGradient>
    <linearGradient id="fold-shade" x1="0" y1="0" x2="1" y2="0">
      <stop offset="0" stop-color="#000" stop-opacity="0"/>
      <stop offset="1" stop-color="#000" stop-opacity="0.13"/>
    </linearGradient>
  </defs>

  <!-- pages -->
  <rect class="page-back" x="0" y="0" width="661" height="855" fill="var(--paper)"/>
  <rect class="page-front" x="661" y="0" width="661" height="855" fill="var(--paper)"/>

  <!-- back cover photo area -->
  <polygon role="img" aria-label="Photo: looking up at a glass office tower against a cloudy sky"
           points="0,0 661,0 661,472 0,360" fill="url(#tower-tones)"/>
  <polygon class="band-pale" points="0,360 661,472 661,490 0,383" fill="var(--mist)"/>
  <polygon class="band-navy" points="0,383 661,472 661,550 0,600" fill="var(--navy)"/>
  <polygon class="band-sky" points="0,600 661,550 661,580 0,637" fill="var(--sky)"/>
  <polygon class="band-mist" points="0,637 661,580 661,590 0,640" fill="var(--mist)"/>

  <!-- front cover photo area -->
  <polygon role="img" aria-label="Photo: a fountain pen resting on business papers beside a laptop"
           points="661,0 1322,0 1322,380 661,460" fill="url(#desk-tones)"/>
  <polygon class="band-pale" points="661,460 1322,380 1322,402 661,490" fill="var(--mist)"/>
  <polygon class="band-sky" points="661,490 1322,402 1322,440 661,490" fill="var(--sky)"/>
  <polygon class="band-navy" points="661,490 1322,440 1322,657 661,550" fill="var(--navy)"/>
  <polygon class="band-sky" points="661,550 752,565 661,580" fill="var(--sky)"/>
  <polygon class="band-mist" points="752,565 1322,657 1322,680" fill="var(--mist)"/>

  <!-- fold shadow -->
  <rect class="fold" x="560" y="0" width="101" height="855" fill="url(#fold-shade)"/>

  <!-- contact block -->
  <rect class="contact-frame" x="107" y="495" width="446" height="316" fill="none" stroke="var(--ice)" stroke-width="1.2"/>
  <text class="heading-bold" x="153" y="527">CONTACT</text>
  <text class="heading-light" x="153" y="560">US</text>

  <g class="office">
    <circle class="icon" cx="154" cy="653" r="6"/>
    <circle cx="154" cy="652" r="1.8" fill="var(--sky)"/>
    <text class="office-name" x="165" y="658">Riverton Office</text>
    <text class="office-line" x="165" y="679">418 North Harbor Street, Suite 200</text>
    <text class="office-line" x="165" y="699">Riverton, NC 27501</text>
  </g>
  <g class="office">
    <circle class="icon" cx="154" cy="738" r="6"/>
    <circle cx="154" cy="737" r="1.8" fill="var(--sky)"/>
    <text class="office-name" x="164" y="743">Oakmere Office</text>
    <text class="office-line" x="164" y="764">36 Linden Row</text>
    <text class="office-line" x="164" y="784">Oakmere, NC 27599</text>
  </g>

  <g class="contact-channel">
    <circle class="icon" cx="474" cy="653" r="8"/>
    <ellipse class="icon" cx="474" cy="653" rx="3.5" ry="8"/>
    <line class="icon" x1="466" y1="653" x2="482" y2="653"/>
    <text class="contact-item" x="474" y="677">www.moreno-legal.example</text>
  </g>
  <g class="contact-channel">
    <circle class="icon" cx="474" cy="707" r="8"/>
    <rect class="icon" x="469" y="703.5" width="10" height="7"/>
    <polyline class="icon" points="469,703.5 474,708 479,703.5"/>
    <text class="contact-item" x="474" y="731">info@moreno-legal.example</text>
  </g>
  <g class="contact-channel">
    <circle class="icon" cx="474" cy="761" r="8"/>
    <path class="icon" d="M470.5 757 q-1 5 6 9 l2 -2 -2.5 -2 -1.5 1 q-2 -1.5 -3 -3.5 l1 -1.5 -2 -2.5 z"/>
    <text class="contact-item" x="474" y="788">555-014-0199</text>
  </g>

  <!-- front cover headline -->
  <text x="991" y="75" text-anchor="middle"><tspan class="tagline-bold">SOLUTIONS</tspan><tspan class="tagline-light"> FOR</tspan></text>
  <text class="tagline-large" x="991" y="114">GROWING BUSINESSES</text>

  <!-- web link rule -->
  <line x1="661" y1="531" x2="1078" y2="531" stroke="#4d86c8" stroke-width="1.2"/>
  <circle cx="1080" cy="531" r="3" fill="var(--sky)"/>
  <text class="web-link" x="1090" y="537">www.moreno-legal.example</text>

  <!-- announcement and name -->
  <text class="announce" x="992" y="713">The Law Office of Dana Moreno, PLLC is now</text>
  <text class="announce" x="992" y="730">known as</text>
  <rect x="846" y="748" width="40" height="40" fill="var(--brand-blue)"/>
  <text class="brand-name" x="896" y="784">MORENO.LAW</text>
</svg>
</body>
</html>
```